Building Servicess

We need a new business card design for a company. We specialise in: Electrical/Site temporary electrics, Data/Network Installation, Passive Fire Protection

Industry/Entity Type

Construction

Contact Information for Business Card

Services provided as detailed on project description

Font styles to use
Serif

Colors
0054AA
0677BA
7BADD7
CADEEF
E8F1F8
00AB8E
00BBA5
67D7C9
C6EFE9
E9F9F6
EB3D1F
EC4F4E
F09395
F8D3D4
FCEDEE

Requirements
Must have
• Company logo-contact details-phone numbers

```html
<!DOCTYPE html>
<html lang="en">
<head>
<meta charset="utf-8">
<title>Northgate Site Services – Business Card</title>
<link rel="stylesheet" href="https://fonts.googleapis.com/css2?family=Montserrat:wght@400;500;600&display=swap">
<style>
  :root {
    --backdrop: #2a2b2f;
    --card: #1c1c1e;
    --frame: #1577c9;
    --accent: #1a7fd4;
    --ink: #f2f2f2;
    --ink-soft: #c9c9cc;
  }
  * { margin: 0; padding: 0; box-sizing: border-box; }
  html, body {
    width: 1200px; height: 786px; overflow: hidden;
    background: var(--backdrop);
    font-family: "Montserrat", sans-serif;
  }
  .canvas {
    width: 1200px; height: 786px;
    display: flex; align-items: center; justify-content: center; gap: 24px;
  }
  .card {
    width: 558px; height: 320px;
    background: var(--card);
    border: 12px solid var(--frame);
    position: relative;
    color: var(--ink);
  }
  /* Front */
  .card-front { display: flex; align-items: center; }
  .brand {
    width: 260px; padding-left: 34px;
    display: flex; align-items: center; gap: 10px;
  }
  .brand-square { width: 14px; height: 14px; background: var(--accent); flex: none; }
  .brand-name {
    color: var(--accent); font-weight: 600; font-size: 17px;
    letter-spacing: 1px; text-transform: uppercase; line-height: 1.3;
  }
  .divider { width: 1px; height: 150px; background: var(--accent); margin-right: 26px; }
  .contact { font-size: 12.5px; line-height: 1.55; color: var(--ink); }
  .person-name {
    color: var(--accent); font-weight: 600; font-size: 21px;
    letter-spacing: 1px; text-transform: uppercase; line-height: 1.2;
  }
  .person-role { margin-bottom: 6px; }
  .address { margin-bottom: 6px; }
  .contact-line { display: flex; align-items: center; gap: 7px; }
  .contact-line svg { width: 11px; height: 11px; flex: none; }
  /* Back */
  .card-back { display: flex; flex-direction: column; align-items: center; justify-content: center; }
  .back-name {
    font-weight: 500; font-size: 30px; letter-spacing: 3px;
    text-transform: uppercase; color: var(--ink-soft); margin-bottom: 46px;
  }
  .services {
    position: absolute; bottom: 26px; left: 0; right: 0;
    text-align: center; font-size: 12.5px; letter-spacing: 0.6px;
    text-transform: uppercase; line-height: 1.6;
  }
  .services .sep { color: var(--accent); padding: 0 4px; }
</style>
</head>
<body>
<main class="canvas">
  <section class="card card-front">
    <div class="brand">
      <span class="brand-square"></span>
      <span class="brand-name">Northgate Site<br>Services Ltd</span>
    </div>
    <div class="divider"></div>
    <div class="contact">
      <div class="person-name">Daniel Mercer</div>
      <div class="person-role">Director</div>
      <div class="address">1420 Alder Lane<br>Salem, OR 97301</div>
      <div class="contact-line">
        <svg viewBox="0 0 24 24" fill="var(--accent)" aria-hidden="true"><path d="M6.6 10.8a15 15 0 0 0 6.6 6.6l2.2-2.2a1 1 0 0 1 1-.25 11.4 11.4 0 0 0 3.6.57 1 1 0 0 1 1 1V20a1 1 0 0 1-1 1A17 17 0 0 1 3 4a1 1 0 0 1 1-1h3.5a1 1 0 0 1 1 1c0 1.25.2 2.45.57 3.57a1 1 0 0 1-.25 1z"/></svg>
        <span>503.555.0142</span>
      </div>
      <div class="contact-line">
        <svg viewBox="0 0 24 24" fill="none" stroke="var(--accent)" stroke-width="2" aria-hidden="true"><rect x="3" y="5" width="18" height="14"/><path d="M3 6l9 7 9-7"/></svg>
        <span>info@northgatesite.com</span>
      </div>
      <div class="contact-line">
        <svg viewBox="0 0 24 24" fill="none" stroke="var(--accent)" stroke-width="2" aria-hidden="true"><circle cx="12" cy="12" r="9"/><path d="M3 12h18M12 3c3 3 3 15 0 18M12 3c-3 3-3 15 0 18"/></svg>
        <span>www.northgatesite.com</span>
      </div>
    </div>
  </section>

  <section class="card card-back">
    <div class="back-name">Northgate</div>
    <div class="services">
      Electrical/Site Temporary Electrics<br>
      Data/Network Installation<span class="sep">|</span>Passive Fire Protection
    </div>
  </section>
</main>
</body>
</html>
```